Business Card for Wellness Clinic

We need a business card for our new logo. I want it to match the feel of the logo

Target Market(s)

Young professional families looking for holistic health care

Industry/Entity Type

Health And Wellness

Contact Information for Business Card

Our business Name: Brackenfield Health & wellness Centre, our phone #, email address...see attached old business card

Font styles to use
Sans Serif

Colors
33b8a4
cee9f5

Requirements
Must have
• my logo and business name
• Font is "Helvetica Neue LT Std 45 Light" and
• Only for "&" using font "Trajan pro bold"
• Use colors in the logo

```html
<!DOCTYPE html>
<html lang="en">
<head>
<meta charset="utf-8">
<title>Brackenfield Health &amp; wellness Centre – Business Cards</title>
<link rel="stylesheet" href="https://fonts.googleapis.com/css2?family=Roboto:wght@300;400&family=Roboto+Condensed:wght@300;400&display=swap">
<style>
  :root {
    --teal: #2fb5a1;
    --ink: #2a2a2a;
    --muted: #555555;
    --paper: #ffffff;
    --backdrop: #2b2b2b;
  }
  * { margin: 0; padding: 0; box-sizing: border-box; }
  html, body { width: 1200px; height: 1055px; overflow: hidden; background: var(--backdrop); }
  body { position: relative; font-family: "Roboto", Arial, sans-serif; color: var(--ink); }

  .card {
    position: absolute;
    left: 210px;
    width: 780px;
    height: 446px;
    background: var(--paper);
    overflow: hidden;
  }
  .card--appointment { top: 50px; }
  .card--contact { top: 559px; }

  .brand {
    position: absolute;
    display: flex;
    align-items: center;
    gap: 14px;
    color: var(--teal);
    font-family: "Roboto", Arial, sans-serif;
    font-weight: 300;
  }
  .brand__mark { width: 16px; height: 16px; background: var(--teal); flex: none; }
  .card--appointment .brand { left: 70px; top: 70px; font-size: 30px; letter-spacing: 1px; }

  .field {
    position: absolute;
    left: 70px;
    display: flex;
    align-items: flex-end;
    font-family: "Roboto Condensed", Arial, sans-serif;
    font-style: italic;
    font-weight: 300;
    font-size: 20px;
  }
  .field__line { flex: 1; border-bottom: 1px solid var(--ink); margin-left: 8px; height: 1px; margin-bottom: 5px; }
  .field--date { top: 210px; width: 400px; }
  .field--time { top: 210px; left: 490px; width: 220px; }
  .field--for { top: 262px; width: 640px; }

  .notice {
    position: absolute;
    left: 30px; right: 30px; top: 322px;
    text-align: center;
    font-family: "Roboto Condensed", Arial, sans-serif;
    font-weight: 400;
    font-size: 19px;
    line-height: 1.4;
  }
  .notice__line { display: block; white-space: nowrap; }

  .card--contact .brand { left: 60px; top: 160px; font-size: 24px; width: 330px; line-height: 1.3; align-items: flex-start; }
  .card--contact .brand__mark { margin-top: 8px; }

  .divider {
    position: absolute;
    left: 400px; top: 60px;
    width: 1px; height: 220px;
    background: linear-gradient(to bottom, transparent, var(--teal) 30%, var(--teal) 70%, transparent);
  }
  .person { position: absolute; left: 430px; top: 70px; font-family: "Roboto Condensed", Arial, sans-serif; }
  .person__name { color: var(--teal); font-size: 22px; font-weight: 400; }
  .person__title { color: var(--ink); font-size: 17px; font-weight: 300; margin-bottom: 14px; }
  .contact-list { list-style: none; }
  .contact-list li { display: flex; align-items: center; gap: 12px; font-size: 20px; font-weight: 300; line-height: 1.4; white-space: nowrap; }
  .contact-list svg { width: 16px; height: 16px; flex: none; fill: none; stroke: var(--ink); stroke-width: 1.4; }

  .address-band {
    position: absolute;
    left: 0; right: 0; top: 320px;
    height: 66px;
    background: var(--teal);
    color: var(--paper);
    display: flex; align-items: center; justify-content: center;
    font-family: "Roboto Condensed", Arial, sans-serif;
    font-weight: 300;
    font-size: 26px;
    letter-spacing: 0.3px;
    white-space: nowrap;
  }
</style>
</head>
<body>

<section class="card card--appointment">
  <div class="brand"><span class="brand__mark"></span><span>Brackenfield Health &amp; wellness Centre</span></div>
  <div class="field field--date">Date:<span class="field__line"></span></div>
  <div class="field field--time">Time:<span class="field__line"></span></div>
  <div class="field field--for">For:<span class="field__line"></span></div>
  <p class="notice">
    <span class="notice__line">If you are unable to keep your appointment, please provide at least 2 business days</span>
    <span class="notice__line">notice or full visit fees will apply.</span>
  </p>
</section>

<section class="card card--contact">
  <div class="brand"><span class="brand__mark"></span><span>Brackenfield Health &amp; wellness Centre</span></div>
  <div class="divider"></div>
  <div class="person">
    <div class="person__name">Dr. Maren Holt, N.D.</div>
    <div class="person__title">Naturopathic Doctor</div>
    <ul class="contact-list">
      <li><svg viewBox="0 0 16 16"><rect x="4" y="1" width="8" height="14" rx="1.5"/><line x1="7" y1="12.5" x2="9" y2="12.5"/></svg>613-555-0184</li>
      <li><svg viewBox="0 0 16 16"><rect x="1" y="3.5" width="14" height="9"/><polyline points="1,3.5 8,9 15,3.5"/></svg>mholt@brackenfieldwellness.ca</li>
      <li><svg viewBox="0 0 16 16"><circle cx="8" cy="8" r="6.5"/><ellipse cx="8" cy="8" rx="3" ry="6.5"/><line x1="1.5" y1="8" x2="14.5" y2="8"/></svg>www.brackenfieldwellness.ca</li>
    </ul>
  </div>
  <div class="address-band">48 Alder Row, Suite 210, Ottawa, ON K1R 3T7</div>
</section>

</body>
</html>
```